Calm and Compass Health Flyer (new business startup)

One page...clear enough to be read if faxed. This mental health clinic treats depression/anxiety in kids and adults. It also treats opiate and alcohol addiction. It's in downtown Elmira, NY and the owner of the clinic is from Elmira NY, where it's located. This clinic does not take health insurance, so it charges a low rate of $75 a visit once they pay the $125 starting fee.

Target Market(s)

doctors offices, new patients

Industry/Entity Type

Doctor

Requirements
Must have
• see microsoft word document. pdf is printed on the company letterhead.
Nice to have
• a simplified map would be nice. if you can include the building it would be a plus. The same two fonts were used in the business cards and letter head (kennedy small caps boo*) and Refrigerator Delux.

```html
<!DOCTYPE html>
<html lang="en">
<head>
<meta charset="utf-8">
<title>Calm and Compass Health Flyer</title>
<link href="https://fonts.googleapis.com/css2?family=Jost:wght@400;500;600;700&display=swap" rel="stylesheet">
<style>
  :root {
    --orange: #ea6a2f;
    --blue: #2b9bd3;
    --ink: #222222;
    --paper: #ffffff;
    --backdrop: #e4e4e4;
    --photo-cool: #dfe6ec;
    --photo-warm: #9a5a46;
    --sky: #6fa6de;
    --map: #eceff1;
  }
  * { margin: 0; padding: 0; box-sizing: border-box; }
  html, body { width: 1200px; height: 1200px; overflow: hidden; background: var(--backdrop); }
  body { font-family: "Jost", Arial, sans-serif; color: var(--ink); position: relative; }

  .flyer { position: absolute; left: 197px; top: 30px; width: 806px; height: 1140px; background: var(--paper); overflow: hidden; }

  .brand { position: absolute; left: 40px; top: 150px; display: flex; align-items: center; gap: 10px; }
  .brand-dot { width: 36px; height: 36px; border-radius: 50%; background: var(--orange); }
  .brand-name { font-weight: 700; font-size: 21px; color: var(--orange); letter-spacing: .2px; white-space: nowrap; }

  .name-panel { position: absolute; left: 390px; top: 80px; width: 380px; height: 210px; background: var(--orange); color: #fff; padding: 28px 28px; }
  .name-panel h1 { font-weight: 500; font-size: 30px; line-height: 1.12; letter-spacing: 1px; white-space: nowrap; }
  .name-panel p { font-size: 15px; margin-top: 12px; line-height: 1.35; }

  .photo-team { position: absolute; left: 40px; top: 210px; width: 350px; height: 370px; background: linear-gradient(160deg, #f2f4f6, var(--photo-cool) 60%, #b9c4cc); }
  .photo-building { position: absolute; left: 390px; top: 290px; width: 416px; height: 240px; background: linear-gradient(180deg, var(--sky) 0%, #b9cbe0 30%, var(--photo-warm) 45%, #7d4b3c 75%, #8a8d90 100%); }

  .prices { position: absolute; right: 40px; top: 542px; text-align: right; font-weight: 700; font-size: 38px; color: var(--orange); line-height: 1.05; }

  .tag { position: absolute; background: var(--blue); color: #fff; font-weight: 600; font-size: 19px; padding: 3px 16px; }
  .hours-tag { left: 40px; top: 602px; }
  .hours { position: absolute; left: 40px; top: 636px; font-size: 24px; font-weight: 500; color: var(--orange); }
  .service { position: absolute; left: 40px; font-size: 25px; color: var(--blue); font-weight: 700; display: flex; align-items: baseline; width: 470px; white-space: nowrap; }
  .service small { font-size: 19px; font-weight: 400; color: var(--ink); margin-left: 6px; }
  .service .leader { flex: 1; border-bottom: 1.5px dashed var(--ink); margin: 0 0 6px 4px; }
  .ages { position: absolute; left: 40px; top: 760px; font-size: 30px; color: var(--blue); }
  .ages strong { color: var(--orange); font-weight: 700; }

  .map { position: absolute; left: 540px; top: 640px; width: 230px; height: 160px; background: linear-gradient(135deg, var(--map), #dde3e8 55%, #a9cde8); }

  .conditions-tag { left: 40px; top: 810px; }
  .conditions { position: absolute; list-style: none; font-size: 20px; line-height: 1.3; }
  .conditions.left { left: 58px; top: 846px; }
  .conditions.right { left: 380px; top: 812px; }
  .conditions li { display: flex; align-items: center; gap: 10px; }
  .conditions svg { width: 16px; height: 16px; flex: none; }

  .motto { position: absolute; left: 40px; top: 960px; font-size: 17px; color: var(--blue); font-style: italic; }
  .footnote { position: absolute; left: 40px; top: 986px; width: 726px; font-size: 11px; line-height: 1.3; }

  .footer { position: absolute; left: 0; top: 1040px; width: 806px; height: 100px; background: var(--blue); color: #fff; display: flex; align-items: center; padding: 0 40px; gap: 28px; }
  .footer .phone { font-size: 30px; font-weight: 500; display: flex; align-items: center; gap: 12px; letter-spacing: 1px; white-space: nowrap; }
  .footer .divider { width: 1px; height: 42px; background: rgba(255,255,255,.7); }
  .footer .web { font-size: 19px; display: flex; align-items: center; gap: 10px; white-space: nowrap; }
  .footer .follow { margin-left: auto; font-size: 17px; text-align: center; }
  .follow-dots { display: flex; gap: 8px; margin-top: 4px; justify-content: center; }
  .follow-dots span { width: 18px; height: 18px; border-radius: 50%; background: #fff; }
</style>
</head>
<body>
<main class="flyer">
  <div class="brand"><span class="brand-dot"></span><span class="brand-name">CALM &amp; COMPASS HEALTH</span></div>

  <div class="photo-team" role="img" aria-label="Photo of two clinicians in white coats"></div>

  <section class="name-panel">
    <h1>DANIEL<br>ORVIS, RPA, PLLC</h1>
    <p>Psychiatric Physician Assistant<br>(PA-C, PSY-CQA)</p>
  </section>

  <div class="photo-building" role="img" aria-label="Photo of the downtown brick clinic building"></div>

  <div class="prices"><div>$125*</div><div>$75*</div></div>

  <div class="tag hours-tag">Hours:</div>
  <div class="hours">Monday and Saturdays 9-4pm</div>
  <div class="service" style="top:670px">Psychiatric Evaluation<small>(45min)</small><span class="leader"></span></div>
  <div class="service" style="top:712px">Psychiatric Office Visit<small>(15min)</small><span class="leader"></span></div>
  <div class="ages"><strong>Ages:</strong> 6 years old and up</div>

  <div class="map" role="img" aria-label="Street map of downtown with the clinic location marked"></div>

  <div class="tag conditions-tag">Conditions Treated:</div>
  <ul class="conditions left">
    <li><svg viewBox="0 0 16 16"><circle cx="8" cy="8" r="8" fill="#ea6a2f"/><path d="M4.5 8.2l2.3 2.3 4.7-4.7" stroke="#fff" stroke-width="2" fill="none"/></svg>Depression</li>
    <li><svg viewBox="0 0 16 16"><circle cx="8" cy="8" r="8" fill="#ea6a2f"/><path d="M4.5 8.2l2.3 2.3 4.7-4.7" stroke="#fff" stroke-width="2" fill="none"/></svg>Anxiety</li>
    <li><svg viewBox="0 0 16 16"><circle cx="8" cy="8" r="8" fill="#ea6a2f"/><path d="M4.5 8.2l2.3 2.3 4.7-4.7" stroke="#fff" stroke-width="2" fill="none"/></svg>Childhood Mood Disorders</li>
    <li><svg viewBox="0 0 16 16"><circle cx="8" cy="8" r="8" fill="#ea6a2f"/><path d="M4.5 8.2l2.3 2.3 4.7-4.7" stroke="#fff" stroke-width="2" fill="none"/></svg>Addiction</li>
  </ul>
  <ul class="conditions right">
    <li><svg viewBox="0 0 16 16"><circle cx="8" cy="8" r="8" fill="#ea6a2f"/><path d="M4.5 8.2l2.3 2.3 4.7-4.7" stroke="#fff" stroke-width="2" fill="none"/></svg>PTSD</li>
    <li><svg viewBox="0 0 16 16"><circle cx="8" cy="8" r="8" fill="#ea6a2f"/><path d="M4.5 8.2l2.3 2.3 4.7-4.7" stroke="#fff" stroke-width="2" fill="none"/></svg>Bipolar</li>
    <li><svg viewBox="0 0 16 16"><circle cx="8" cy="8" r="8" fill="#ea6a2f"/><path d="M4.5 8.2l2.3 2.3 4.7-4.7" stroke="#fff" stroke-width="2" fill="none"/></svg>ADHD</li>
    <li><svg viewBox="0 0 16 16"><circle cx="8" cy="8" r="8" fill="#ea6a2f"/><path d="M4.5 8.2l2.3 2.3 4.7-4.7" stroke="#fff" stroke-width="2" fill="none"/></svg>Disorders</li>
  </ul>

  <p class="motto">“We work for you, not the insurance companies”</p>
  <p class="footnote">*Although we do not partner with any Health Insurance Companies at this time, a bill will be provided to you at the time of service for you to submit to your insurance company.</p>

  <footer class="footer">
    <div class="phone">
      <svg width="28" height="28" viewBox="0 0 24 24"><circle cx="12" cy="12" r="11" fill="none" stroke="#fff" stroke-width="1.8"/><path d="M8 6.5l2 .3 1 2.6-1.3 1.1a7 7 0 0 0 3.8 3.8l1.1-1.3 2.6 1 .3 2c-.2.7-1 1.2-1.8 1.2A10 10 0 0 1 6.8 8.3c0-.8.5-1.6 1.2-1.8z" fill="#fff"/></svg>
      607 555 0148
    </div>
    <span class="divider"></span>
    <div class="web">
      <svg width="20" height="20" viewBox="0 0 24 24" fill="none" stroke="#fff" stroke-width="1.8"><circle cx="12" cy="12" r="10"/><ellipse cx="12" cy="12" rx="4.5" ry="10"/><path d="M2 12h20M4 7h16M4 17h16"/></svg>
      www.calm-compass.com
    </div>
    <span class="divider"></span>
    <div class="follow">Follow Us:<div class="follow-dots"><span></span><span></span><span></span></div></div>
  </footer>
</main>
</body>
</html>
```